Creative 1 page website design with html coding needed to go with Game Pre-Registration App

Early Bird Lounge
~Discover games before release~

Website keywords: Simple, slick, stylish
Colors: Black, white, pink (like our logo)

***draft can be created in PSD or HTML***

We have a brand new service called Early Bird Lounge which will be a game app pre-registration service. We already have the icon & UI for the app and we are looking for a slick & stylish corporate website to go with the service.

This will be a corporate website aim for businesses to contact us. Consumers will not be able to pre-register for games here. We do however want consumers to download our app from Nimbus Arcade after landing here.

Some framework we have in mind for 1 page website:
Home - default page showing the UI of the app and Nimbus Arcade icon with store link.
Our Service - quick explanation about our service & it's strength
Clients - logos of our clients
Press-
Pricing - basic usage is free. There will be premium services customers can use on a performance basis (CPA).
Contact Us

Call to action will be 1. Download the app 2. Contact us

We would like to be able to edit the press and clients section with web developer's support.

website in image:
https://www.velquorin.com/

Target Market(s)

Marketing managers of game developer. We want game developers to find out about our service and get in touch with us. The service will only be available in USA.

Midcore gamers in USA: Our end users will be game enthusiasts from US. Male aged 15-35.

Industry/Entity Type

Games

Font styles to use
Sans Serif

Colors
000000
ffffff
e567a6
e34097

Requirements
Must have
• - Only use our colors from the logo attached.
- UI of our app with an Zephyx phone
- Link to Nimbus Arcade Store
- slick & modern design
- Font used: Century Gothic

```html
<!DOCTYPE html>
<html lang="en">
<head>
<meta charset="utf-8">
<title>Early Bird Lounge — Discover games before release</title>
<link href="https://fonts.googleapis.com/css2?family=Mulish:wght@400;600;700;800&family=Questrial&display=swap" rel="stylesheet">
<style>
:root{
  --pink:#e34097;
  --pink-soft:#e567a6;
  --pink-pale:#f08cbd;
  --black:#000000;
  --ink:#1e1e1e;
  --dark:#2d2d2d;
  --charcoal:#3a3a3a;
  --grey:#777777;
  --grey-light:#e8e8e8;
  --panel:#f3f3f3;
  --white:#ffffff;
  --head:"Mulish",sans-serif;
  --body:"Questrial",sans-serif;
}
*{box-sizing:border-box;margin:0;padding:0}
a{text-decoration:none;color:inherit}
html,body{width:1200px;height:4260px;overflow:hidden}
body{background:var(--white);font-family:var(--body);color:var(--ink);position:relative}
section,header,footer{position:relative;width:1200px;overflow:hidden}
.abs{position:absolute}
.section-title{position:absolute;left:0;width:1200px;text-align:center;font-family:var(--head);font-weight:700;font-size:31px;color:#555}
.section-title::after{content:"";display:block;width:120px;height:5px;background:var(--pink);margin:22px auto 0}

/* hero */
.hero{height:682px;background:linear-gradient(135deg,#3b3b3b 0%,#1c1c1c 60%,#111 100%)}
.brand{left:36px;top:0;width:250px;height:132px;background:var(--black);display:flex;align-items:center;gap:14px;padding-left:22px}
.brand-mark{width:30px;height:30px;background:var(--pink)}
.brand-name{font-family:var(--head);font-weight:800;font-size:27px;color:var(--white);line-height:1.05}
.main-nav{right:28px;top:56px;display:flex;gap:34px;font-family:var(--head);font-size:26px;color:var(--white)}
.main-nav .active{color:var(--pink);border-bottom:3px solid var(--pink);padding-bottom:6px}
.hero-title{left:43px;top:250px;font-family:var(--head);font-weight:800;font-size:56px;line-height:70px;color:var(--white)}
.hero-title em{font-style:normal;color:var(--pink)}
.hero-rule{left:43px;top:405px;width:540px;height:2px;background:var(--pink)}
.hero-copy{left:43px;top:428px;width:580px;font-size:22px;line-height:32px;color:var(--white)}
.store-badges{left:46px;top:548px;display:flex;gap:24px}
.store-badge{display:flex;align-items:center;gap:14px;width:236px;height:70px;background:var(--black);border:2px solid #555;border-radius:8px;padding:0 16px;color:var(--white)}
.store-badge .sq{width:22px;height:22px;background:var(--white);flex:none}
.store-badge small{display:block;font-size:13px;color:#bbb}
.store-badge b{display:block;font-family:var(--head);font-size:21px;font-weight:700;line-height:1.1;white-space:nowrap}
.hero-visual{right:0;top:178px;width:385px;height:504px;background:linear-gradient(160deg,#5a5a5a 0%,#d8b7a8 45%,#2a2a2a 100%)}

/* why */
.why{height:632px;background:var(--white)}
.why .section-title{top:70px}
.features{left:0;top:205px;width:1200px;display:flex;justify-content:center;gap:70px}
.feature{width:330px;text-align:center}
.feature-icon{width:195px;height:195px;border-radius:50%;background:#eeeeee;margin:0 auto;display:flex;align-items:center;justify-content:center}
.feature h3{margin-top:68px;font-family:var(--head);font-weight:700;font-size:26px;color:var(--ink);white-space:nowrap}
.feature:first-child h3{color:var(--pink)}
.feature p{margin:10px auto 0;width:260px;font-size:18px;line-height:24px;color:#333}

/* facts */
.facts{height:798px;background:var(--panel)}
.facts .section-title{top:70px}
.facts-visual{left:0;top:124px;width:480px;height:674px;background:linear-gradient(150deg,#333 0%,#4a4a4a 40%,#e3b9a4 75%,#f3f3f3 100%)}
.facts-heading{left:490px;top:226px;font-family:var(--head);font-weight:700;font-size:38px;color:var(--ink)}
.facts-copy{left:490px;top:290px;width:660px;font-size:21px;line-height:30px;color:#333}
.donut{top:430px;width:280px;height:280px}
.donut svg{position:absolute;inset:0}
.donut-label{position:absolute;inset:0;display:flex;flex-direction:column;align-items:center;justify-content:center;color:var(--pink)}
.donut-label strong{font-family:var(--head);font-weight:400;font-size:60px;line-height:1}
.donut-label span{width:150px;border-top:2px solid var(--pink);margin-top:10px;padding-top:6px;text-align:center;font-family:var(--head);font-size:34px;line-height:1.1}

/* testimonial */
.testimonial{height:402px}
.quote-panel{left:0;top:0;width:800px;height:402px;background:var(--pink-soft)}
.quote-mark{left:235px;top:20px;font-family:var(--head);font-size:140px;color:#d7559a;line-height:1}
.avatar{left:48px;top:70px;width:165px;height:165px;border-radius:50%;border:7px solid var(--white);background:linear-gradient(160deg,#d9b3a0,#8a6a5a)}
.quote-text{left:252px;top:48px;width:520px;font-family:var(--head);font-size:27px;line-height:37px;color:var(--white)}
.quote-author{left:252px;top:264px;font-size:15px;color:var(--white)}
.quote-dots{left:252px;top:306px;display:flex;gap:12px}
.quote-dots i{width:22px;height:22px;border-radius:50%;background:#7a2a55}
.quote-dots i:first-child{background:#3a1029}
.quote-arrows{left:688px;top:306px;display:flex;gap:8px}
.quote-arrows i{width:32px;height:32px;background:var(--pink);display:flex;align-items:center;justify-content:center}
.client-panel{left:800px;top:0;width:400px;height:402px;background:var(--charcoal);display:flex;align-items:center;justify-content:center;gap:18px}
.client-panel .sq{width:58px;height:58px;background:var(--pink)}
.client-panel b{font-family:var(--head);font-weight:700;font-size:54px;color:var(--white)}

/* clients */
.clients{height:184px;background:var(--white);border-bottom:2px solid var(--grey-light)}
.client-logos{left:40px;top:0;width:1120px;height:184px;display:flex;align-items:center;justify-content:space-between}
.client-logos span{font-family:var(--head);font-weight:700;font-size:30px;color:#666}

/* news */
.news{height:852px;background:var(--white)}
.news .section-title{top:100px}
.news-cards{left:46px;top:232px;display:flex;gap:71px}
.news-card{width:320px}
.news-media{position:relative;height:176px;background:linear-gradient(135deg,#4fc3e0,#e6ebee 55%,#f2a04a)}
.news-card:nth-child(2) .news-media{background:linear-gradient(135deg,#f1c56a,#e7e2d8 50%,#58b9c9)}
.news-card:nth-child(3) .news-media{background:linear-gradient(135deg,#a7dbe4,#f0efe6 50%,#e9614f)}
.news-date{position:absolute;left:20px;top:16px;width:70px;height:70px;border-radius:50%;background:var(--pink);color:var(--white);text-align:center;font-family:var(--head);font-size:16px;line-height:1;padding-top:14px}
.news-date b{display:block;font-size:24px;margin-top:4px}
.news-card h3{margin-top:40px;font-family:var(--head);font-weight:700;font-size:26px;line-height:32px;color:var(--ink)}
.news-card p{margin-top:14px;font-size:16px;line-height:21px;color:#555}
.news-card hr{border:none;height:4px;background:#cfcfcf;width:120px;margin:18px 0 0 100px}
.news-dots{left:0;top:788px;width:1200px;display:flex;justify-content:center;gap:18px}
.news-dots i{width:26px;height:26px;border-radius:50%;background:#cfcfcf}
.news-dots i:first-child{background:var(--pink)}

/* contact */
.contact{height:380px;background:linear-gradient(135deg,#3b3b3b,#585858 45%,#2a2a2a)}
.contact h2{position:absolute;left:0;top:30px;width:1200px;text-align:center;font-family:var(--head);font-weight:700;font-size:84px;color:var(--white)}
.contact p{position:absolute;left:0;top:155px;width:1200px;text-align:center;font-size:22px;color:var(--white)}
.contact-btn{left:492px;top:236px;width:215px;height:88px;border:3px solid var(--pink);background:rgba(0,0,0,.35);color:var(--white);font-family:var(--head);font-size:24px;display:flex;align-items:center;justify-content:center}

/* social */
.social{height:74px;display:flex}
.social span{flex:1;display:flex;align-items:center;justify-content:center;font-family:var(--head);font-weight:700;font-size:24px;color:var(--white)}
.social span:nth-child(1){background:#e34097}
.social span:nth-child(2){background:#e567a6}
.social span:nth-child(3){background:#ea7fb3}
.social span:nth-child(4){background:#f08cbd}

/* footer */
.site-footer{height:238px;background:var(--panel)}
.footer-brand{left:0;top:26px;width:1200px;text-align:center;font-family:var(--head);font-weight:800;font-size:26px;color:#9a9a9a}
.footer-nav{left:0;top:110px;width:1200px;display:flex;justify-content:center;gap:95px;font-family:var(--head);font-size:24px;color:#666}
.footer-nav .active{color:var(--pink);border-bottom:3px solid var(--pink);padding-bottom:4px}
.copyright{left:0;top:198px;width:1200px;height:40px;background:var(--pink);color:var(--white);font-size:14px;display:flex;align-items:center;justify-content:center}
</style>
</head>
<body>

<header class="hero">
  <div class="abs brand"><span class="brand-mark"></span><span class="brand-name">Early Bird<br>Lounge</span></div>
  <nav class="abs main-nav"><span class="active">Home</span><span>Our Service</span><span>Clients</span><span>Press</span><span>Contact Us</span></nav>
  <h1 class="abs hero-title">Reach The Highly<br>Engaged <em>Audience</em></h1>
  <div class="abs hero-rule"></div>
  <p class="abs hero-copy">Lorem ipsum dolor sit amet, consectetuer adipiscing elit, sed diam nonummy nibh euismod tincidunt.</p>
  <div class="abs store-badges">
    <a class="store-badge" href="https://www.velquorin.com/"><span class="sq"></span><span><small>Get it on</small><b>Nimbus Arcade</b></span></a>
    <a class="store-badge" href="https://www.velquorin.com/"><span class="sq"></span><span><small>Get it for</small><b>Zephyx</b></span></a>
  </div>
  <div class="abs hero-visual" role="img" aria-label="Hand holding a Zephyx phone showing the Early Bird Lounge app game list"></div>
</header>

<section class="why">
  <h2 class="section-title">Why Should You Chose Us!</h2>
  <div class="abs features">
    <div class="feature">
      <div class="feature-icon"><svg width="90" height="90" viewBox="0 0 90 90" fill="none" stroke="#e34097" stroke-width="4"><rect x="8" y="6" width="56" height="62" rx="3"/><rect x="40" y="26" width="34" height="50" rx="3"/><rect x="16" y="16" width="20" height="16"/><path d="M58 62l6 18 4-8 8-2z" fill="#333" stroke="#333" stroke-width="2"/></svg></div>
      <h3>100% Cross-Platform</h3>
      <p>Lorem ipsum dolor sit amet, consectetuer adipiscing elit</p>
    </div>
    <div class="feature">
      <div class="feature-icon"><svg width="90" height="90" viewBox="0 0 90 90" fill="none" stroke="#555" stroke-width="4"><rect x="10" y="10" width="70" height="56" rx="3"/><circle cx="45" cy="34" r="10"/><path d="M38 44l-4 24 11-6 11 6-4-24"/><path d="M20 20h10M60 20h10"/></svg></div>
      <h3>High Quality Games</h3>
      <p>Lorem ipsum dolor sit amet, consectetuer adipiscing elit</p>
    </div>
    <div class="feature">
      <div class="feature-icon"><svg width="100" height="90" viewBox="0 0 100 90" fill="none" stroke="#555" stroke-width="4"><path d="M14 48a36 36 0 0 1 72 0"/><path d="M50 48l16-18"/><circle cx="30" cy="62" r="7"/><circle cx="50" cy="58" r="8"/><circle cx="70" cy="62" r="7"/><path d="M18 84c0-8 6-12 12-12s12 4 12 12M38 84c0-10 6-15 12-15s12 5 12 15M58 84c0-8 6-12 12-12s12 4 12 12"/></svg></div>
      <h3>Flawless Performance</h3>
      <p>Lorem ipsum dolor sit amet, consectetuer adipiscing elit</p>
    </div>
  </div>
</section>

<section class="facts">
  <h2 class="section-title">Facts &amp; Figures</h2>
  <div class="abs facts-visual" role="img" aria-label="Hand holding a phone showing a game page in the app"></div>
  <h3 class="abs facts-heading">Reach: Over 700 Million People</h3>
  <p class="abs facts-copy">Lorem ipsum dolor sit amet, consectetuer adipiscing elit, sed diam nonummy nibh euismod tincidunt.</p>
  <div class="abs donut" style="left:492px">
    <svg viewBox="0 0 280 280"><circle cx="140" cy="140" r="125" fill="none" stroke="#8a8a8a" stroke-width="24"/><circle cx="140" cy="140" r="125" fill="none" stroke="#e567a6" stroke-width="24" stroke-dasharray="361.3 785.4" transform="rotate(-90 140 140)"/></svg>
    <div class="donut-label"><strong>46%</strong><span>Female Gamers</span></div>
  </div>
  <div class="abs donut" style="left:872px">
    <svg viewBox="0 0 280 280"><circle cx="140" cy="140" r="125" fill="none" stroke="#8a8a8a" stroke-width="24"/><circle cx="140" cy="140" r="125" fill="none" stroke="#e567a6" stroke-width="24" stroke-dasharray="455.5 785.4" transform="rotate(-90 140 140)"/></svg>
    <div class="donut-label"><strong>58%</strong><span>Male Gamers</span></div>
  </div>
</section>

<section class="testimonial">
  <div class="abs quote-panel"></div>
  <div class="abs quote-mark">&ldquo;</div>
  <div class="abs avatar" role="img" aria-label="Portrait of the content manager quoted"></div>
  <p class="abs quote-text">Lorem ipsum dolor sit amet, consectetuer adipiscing elit, sed diam nonummy nibh euismod tincidunt ut laoreet dolore magna aliquam erat volutpat.</p>
  <div class="abs quote-author">Dana Reyes, Content Manager</div>
  <div class="abs quote-dots"><i></i><i></i><i></i><i></i><i></i></div>
  <div class="abs quote-arrows">
    <i><svg width="14" height="14" viewBox="0 0 14 14"><path d="M10 1L3 7l7 6z" fill="#fff"/></svg></i>
    <i><svg width="14" height="14" viewBox="0 0 14 14"><path d="M4 1l7 6-7 6z" fill="#fff"/></svg></i>
  </div>
  <div class="abs client-panel"><span class="sq"></span><b>Vantora</b></div>
</section>

<section class="clients">
  <div class="abs client-logos"><span>Brightlens</span><span>Ramsey</span><span>Vantora</span><span>Keystrand</span><span>Orla Nutrition</span></div>
</section>

<section class="news">
  <h2 class="section-title">News &amp; Event</h2>
  <div class="abs news-cards">
    <article class="news-card">
      <div class="news-media" role="img" aria-label="Illustration of cloud apps and a megaphone"><div class="news-date">SEP<b>25</b></div></div>
      <h3>Lorem ipsum dolor sit amet lorem</h3>
      <p>Typi non habent claritatem insitam; est usus legentis in iis qui facit eorum claritatem. Investigationes demonstraverunt lectores legere me lius quod ii legunt saepius. Claritas est etiam processus dynamicus, qui sequitur mutationem.</p>
      <hr>
    </article>
    <article class="news-card">
      <div class="news-media" role="img" aria-label="Illustration of hands at a laptop with app icons"><div class="news-date">SEP<b>24</b></div></div>
      <h3>Lorem ipsum dolor sit amet lorem</h3>
      <p>Typi non habent claritatem insitam; est usus legentis in iis qui facit eorum claritatem. Investigationes demonstraverunt lectores legere me lius quod ii legunt saepius. Claritas est etiam processus dynamicus, qui sequitur mutationem.</p>
      <hr>
    </article>
    <article class="news-card">
      <div class="news-media" role="img" aria-label="Illustration of marketing charts and devices"><div class="news-date">SEP<b>23</b></div></div>
      <h3>Lorem ipsum dolor sit amet lorem</h3>
      <p>Typi non habent claritatem insitam; est usus legentis in iis qui facit eorum claritatem. Investigationes demonstraverunt lectores legere me lius quod ii legunt saepius. Claritas est etiam processus dynamicus, qui sequitur mutationem.</p>
      <hr>
    </article>
  </div>
  <div class="abs news-dots"><i></i><i></i><i></i></div>
</section>

<section class="contact" role="img" aria-label="Team working together in an office, dimmed behind the call to action">
  <h2>Get in Touch</h2>
  <p>We're growing... fast! Become a part in our exciting journey and join our talented global team.</p>
  <a class="abs contact-btn" href="https://www.velquorin.com/">Join with us</a>
</section>

<nav class="social"><span>Chatterly</span><span>Flockit</span><span>Circlo</span><span>Linkwork</span></nav>

<footer class="site-footer">
  <div class="abs footer-brand">Early Bird Lounge</div>
  <nav class="abs footer-nav"><span class="active">Home</span><span>Our Service</span><span>Clients</span><span>Press</span><span>Contact Us</span></nav>
  <div class="abs copyright">© 2014 Early Bird Lounge, Inc. &nbsp;|&nbsp; Site Links &nbsp;|&nbsp; Privacy Policy &nbsp;|&nbsp; Terms of use</div>
</footer>

</body>
</html>
```